Introducing Vessa – the virtual restaurant experience at home

Missing going out on dining at your favourite restaurant with your friends, then Vessa Dining is the answer.

While it may not be possible during the COVID-19 pandemic, or when restaurants return as booking opportunities will be hard to get, an innovative new concept gives people the chance to enjoy a virtual restaurant experience at home.

VESSA offers diners the ability to get the restaurant experience at home and restaurants to expand their dining rooms beyond the confines of social distancing

Vessa Dining is an app where you can book your favourite restaurant table, invite your friends and choose your menu and beverages. On the day the restaurant will come to your house, set your table, cook and serve you the menu you have chosen, serve you drinks and clean up, just like you where at the restaurant.

We are looking for 2 similar infographics to explain a process from 2 different perspective

The design needs to be simple, contemporary, imaginative and modern for this concept, it needs to be sophisticated, something that would represent an up-market to fine dining style of restaurant. The designs need to be easily understood using white space to separate the elements

Our preferred colour is attached along with our logos

Infographic 1 - Host Process
1. Host makes reservation at favourite restaurant at home on the Vessa Dining App
2. Select menus and invite guests
3. Confirm either single or shared payment options
4. Booking confirmed with restaurant
5. Host confirms on the App they the required equipment
6. Cook/server arrive 1 hour prior to guests, prepares and sets table
7. Guests arrive and cook/server offer dinks and serves meal
8. Cook/Server cleans up and finalises check with host

Infographic 2 - Restaurant Process
1. Host makes reservation and orders meal
2. Restaurant confirm reservation details
3. Restaurant prepares cuisine and arranges cook/serve waiter
4. Cook/server arrive 1 hour before guests, prepares and sets table
5. Cook/server cooks and serves meals and wine
6. Cook/Server cleans up and finalises check with host

Good Luck

```html
<!DOCTYPE html>
<html lang="en">
<head>
<meta charset="utf-8">
<title>Vessa Dining – Host and Restaurant Process</title>
<link rel="stylesheet" href="https://fonts.googleapis.com/css2?family=PT+Sans:wght@400;700&family=Raleway:wght@300&display=swap">
<style>
  :root {
    --bg-top: #a9006c;
    --bg-mid: #8e0b5c;
    --bg-bottom: #560735;
    --disc: #b0197a;
    --line: #ffffff;
    --label-bg: rgba(160, 10, 105, 0.55);
    --text: #ffffff;
  }
  html, body {
    margin: 0;
    padding: 0;
    overflow: hidden;
  }
  .infographic {
    position: relative;
    width: 965px;
    height: 1200px;
    overflow: hidden;
    background: linear-gradient(180deg, var(--bg-top) 0%, var(--bg-mid) 55%, var(--bg-bottom) 100%);
    font-family: "PT Sans", Arial, sans-serif;
    color: var(--text);
  }
  .brand {
    position: absolute;
    left: 92px;
    top: 46px;
    width: 90px;
    text-align: center;
    font-weight: 700;
    color: var(--text);
    letter-spacing: 3px;
  }
  .brand-dot {
    width: 34px;
    height: 34px;
    margin: 0 auto 8px;
    border-radius: 50%;
    background: var(--text);
  }
  .brand-name {
    font-size: 22px;
    line-height: 1;
  }
  .brand-sub {
    font-size: 9px;
    letter-spacing: 5px;
    margin-top: 3px;
  }
  .flow {
    position: absolute;
    inset: 0;
  }
  .icon {
    fill: none;
    stroke: var(--line);
    stroke-width: 2.2;
    stroke-linecap: round;
    stroke-linejoin: round;
  }
  .icon .solid {
    fill: var(--line);
    stroke: none;
  }
  .step-label {
    position: absolute;
    box-sizing: border-box;
    display: flex;
    align-items: center;
    justify-content: center;
    padding: 4px 6px;
    border: 1px solid var(--line);
    border-radius: 3px;
    background: var(--label-bg);
    font-size: 11px;
    line-height: 1.3;
    text-align: center;
    white-space: nowrap;
  }
  .step-label.left-align {
    justify-content: flex-start;
    text-align: left;
    padding-left: 10px;
  }
  .process-title {
    position: absolute;
    font-family: "Raleway", Arial, sans-serif;
    font-weight: 300;
    font-size: 30px;
    letter-spacing: 1px;
    white-space: nowrap;
    color: var(--text);
  }
  .process-title.host {
    left: 460px;
    top: 520px;
    transform: translate(-50%, -50%) rotate(-90deg);
  }
  .process-title.restaurant {
    left: 543px;
    top: 502px;
    transform: translate(-50%, -50%) rotate(90deg);
  }
</style>
</head>
<body>
<main class="infographic">

  <div class="brand">
    <div class="brand-dot"></div>
    <div class="brand-name">VESSA</div>
    <div class="brand-sub">DINING</div>
  </div>

  <svg class="flow" width="965" height="1200" viewBox="0 0 965 1200">
    <defs>
      <marker id="arrowhead" viewBox="0 0 10 10" refX="8" refY="5" markerWidth="6" markerHeight="6" orient="auto">
        <path d="M0,0 L10,5 L0,10 z" fill="#ffffff"/>
      </marker>
      <g id="table">
        <path d="M-30,4 Q0,-4 30,4 L34,26 Q0,34 -34,26 Z"/>
        <path d="M-22,-8 l0,10 M-27,-16 q5,10 10,0 M22,-8 l0,10 M17,-16 q5,10 10,0"/>
        <path d="M0,-28 L0,2 M-10,-22 q10,12 20,0 M-10,-28 l0,6 M0,-34 l0,6 M10,-28 l0,6"/>
      </g>
    </defs>

    <line x1="227" y1="116" x2="965" y2="116" stroke="#ffffff" stroke-width="2"/>

    <line x1="500" y1="300" x2="500" y2="700" stroke="#ffffff" stroke-width="3"/>
    <line x1="515" y1="836" x2="515" y2="950" stroke="#ffffff" stroke-width="3"/>

    <g fill="none" stroke="#ffffff" stroke-width="3.5" marker-end="url(#arrowhead)">
      <path d="M452,238 Q410,246 388,290"/>
      <path d="M325,352 Q295,372 290,392"/>
      <path d="M236,486 L242,536"/>
      <path d="M280,640 Q295,675 305,690"/>
      <path d="M372,735 Q410,750 446,758"/>
      <path d="M558,254 Q610,275 628,334"/>
      <path d="M665,476 L665,558"/>
      <path d="M612,690 Q595,718 578,735"/>
      <path d="M468,824 Q440,838 420,852"/>
      <path d="M562,824 Q592,834 612,850"/>
      <path d="M420,946 Q445,968 460,980"/>
      <path d="M620,950 Q600,974 572,986"/>
    </g>

    <g stroke="#ffffff" stroke-width="2.5" fill="#b0197a">
      <circle cx="505" cy="246" r="55"/>
      <circle cx="350" cy="319" r="38"/>
      <circle cx="255" cy="431" r="53"/>
      <circle cx="244" cy="594" r="53"/>
      <circle cx="338" cy="713" r="38"/>
      <circle cx="647" cy="406" r="68"/>
      <circle cx="647" cy="630" r="68"/>
      <circle cx="515" cy="768" r="68"/>
      <circle cx="380" cy="888" r="62"/>
      <circle cx="647" cy="885" r="68"/>
      <circle cx="515" cy="1018" r="68"/>
    </g>

    <!-- step icons -->
    <g class="icon" transform="translate(505 246)" role="img" aria-label="Phone with the booking app">
      <rect x="-17" y="-32" width="34" height="60" rx="5"/>
      <line x1="-6" y1="22" x2="6" y2="22"/>
      <circle cx="12" cy="18" r="7"/>
      <circle class="solid" cx="12" cy="18" r="2.5"/>
    </g>
    <g class="icon" transform="translate(350 319)" role="img" aria-label="Menu card with ticks">
      <rect x="-24" y="-20" width="20" height="30"/>
      <path d="M-20,-12 h12 M-20,-6 h12 M-20,0 h12"/>
      <path d="M2,0 l5,6 l10,-14 M4,12 l4,5 l8,-11"/>
    </g>
    <g class="icon" transform="translate(255 431)" role="img" aria-label="Payment card shared between guests">
      <rect x="-34" y="-14" width="38" height="26" rx="3"/>
      <path d="M-29,-6 h20"/>
      <circle class="solid" cx="-6" cy="5" r="3"/>
      <circle class="solid" cx="-1" cy="5" r="3"/>
      <path d="M4,0 h8 M12,-22 v44 M12,-22 h8 M12,0 h8 M12,22 h8"/>
      <circle cx="25" cy="-22" r="5"/>
      <circle cx="25" cy="0" r="5"/>
      <circle cx="25" cy="22" r="5"/>
    </g>
    <g class="icon" transform="translate(244 594)" role="img" aria-label="Confirmed booking card with a tick">
      <path d="M-50,-10 h32 M-50,0 h32 M-50,10 h32 M18,-10 h32 M18,0 h32 M18,10 h32"/>
      <rect x="-18" y="-30" width="36" height="54"/>
      <path d="M-6,8 l6,7 l12,-16"/>
    </g>
    <g class="icon" transform="translate(338 713)" role="img" aria-label="Equipment checklist in the app">
      <circle class="solid" cx="-12" cy="0" r="13"/>
      <path d="M1,0 h8 M9,-15 v30 M9,-15 h6 M9,0 h6 M9,15 h6"/>
      <circle class="solid" cx="21" cy="-15" r="5"/>
      <circle class="solid" cx="21" cy="0" r="5"/>
      <circle class="solid" cx="21" cy="15" r="5"/>
    </g>
    <g class="icon" transform="translate(647 406)" role="img" aria-label="Reservation details with a tick">
      <rect x="-40" y="-38" width="40" height="62"/>
      <path d="M-32,-10 h60 M-32,0 h60 M-32,10 h55 M-32,20 h45"/>
      <path d="M8,22 l10,12 l22,-26"/>
    </g>
    <g class="icon" transform="translate(647 630)" role="img" aria-label="Covered dish and plates">
      <path d="M-30,-4 a22,22 0 0 1 44,0 z M-34,-4 h52 M-8,-26 v-4"/>
      <ellipse cx="-20" cy="22" rx="16" ry="5"/>
      <ellipse cx="20" cy="22" rx="16" ry="5"/>
    </g>
    <g class="icon" transform="translate(515 778)" role="img" aria-label="Dining table laid with glasses and candles">
      <use href="#table"/>
    </g>
    <text x="533" y="740" fill="#ffffff" font-family="PT Sans, Arial, sans-serif" font-size="20" font-weight="700">1h</text>
    <g class="icon" transform="translate(372 894)" role="img" aria-label="Laid table for arriving guests">
      <use href="#table"/>
    </g>
    <g class="icon" transform="translate(647 892)" role="img" aria-label="Table being served">
      <use href="#table"/>
      <path d="M-52,-8 l-8,-4 M-48,-30 l-7,-7 M-30,-46 l-4,-8 M0,-50 v-9 M30,-46 l4,-8 M48,-30 l7,-7 M52,-8 l8,-4"/>
    </g>
    <g class="icon" transform="translate(515 1018)" role="img" aria-label="Finalised bill with a tick">
      <path d="M-60,-10 q8,-6 16,0 t16,0 t10,0 M-62,2 q8,-6 16,0 t16,0 t10,0 M-60,14 q8,-6 16,0 t16,0 t10,0"/>
      <rect x="-18" y="-32" width="36" height="58"/>
      <path d="M-10,-20 h20 M-10,-13 h20"/>
      <path d="M2,10 l7,8 l16,-22"/>
    </g>
  </svg>

  <div class="process-title host">HOST PROCESS</div>
  <div class="process-title restaurant">RESTAURANT PROCESS</div>

  <div class="step-label left-align" style="left:579px; top:218px; width:240px; height:39px;">Host makes reservation at favourite restaurant<br>at home on the Vessa Dining App</div>
  <div class="step-label" style="left:115px; top:278px; width:176px; height:45px;">Select menus and invite guests</div>
  <div class="step-label" style="left:48px; top:405px; width:137px; height:55px;">Confirm either single<br>or shared payment<br>options</div>
  <div class="step-label" style="left:59px; top:571px; width:121px; height:45px;">Booking confirmed<br>with restaurant</div>
  <div class="step-label" style="left:125px; top:697px; width:152px; height:48px;">Host confirms on the App<br>they the required equipment</div>
  <div class="step-label" style="left:726px; top:387px; width:193px; height:40px;">Restaurant confirm reservation details</div>
  <div class="step-label" style="left:735px; top:592px; width:172px; height:53px;">Restaurant prepares cuisine<br>and arranges cook/ serve waiter</div>
  <div class="step-label" style="left:590px; top:749px; width:188px; height:49px;">Cook/server arrive 1 hour prior<br>to guests, prepares and sets table</div>
  <div class="step-label" style="left:143px; top:882px; width:152px; height:47px;">Guests arrive and cook/server<br>offer dinks and serves meal</div>
  <div class="step-label" style="left:741px; top:877px; width:156px; height:51px;">Cook/server cooks<br>and serves meals and wine</div>
  <div class="step-label" style="left:438px; top:1110px; width:152px; height:45px;">Cook/Server cleans up<br>and finalises check with host</div>

</main>
</body>
</html>
```